Design a Pre-Workout Package Design For a Supplement Company!

Create a colourful and energetic design for our pre-workout packaging! A small container that holds 30 servings of pre-workout needs to be designed to be eye-catching and inspirational! We want it to jump off the shelf into your face and scream positivity, energy and colour.

I've attached our logo- QUELVA Performance which should be the face of the package with the colourful packaging behind it! Feel free to change it around! I've also attached a supplement company's pre-workout design that I love! Good luck!!!

Target Market(s)

Fitness goers

Industry/Entity Type

Fitness

Colors

Designer to choose colors to be used in the design.

Requirements
Must have
• -Logo-QUELVA Performance on the front
• - Colourful, energetic, inspiration package

```html
<!DOCTYPE html>
<html lang="en">
<head>
<meta charset="utf-8">
<title>QUELVA Performance Pre-Workout Label</title>
<link rel="stylesheet" href="https://fonts.googleapis.com/css2?family=Russo+One&family=Roboto+Condensed:ital,wght@1,800&display=swap">
<style>
  :root {
    --page: #ecebef;
    --sky: #3fa3e0;
    --royal: #2b3f9e;
    --violet: #6a3a9c;
    --green: #3c9a3e;
    --magenta: #c0245f;
    --orange: #f07a2a;
    --navy: #1e2a5c;
    --red: #c4183f;
    --white: #ffffff;
  }
  * { margin: 0; padding: 0; box-sizing: border-box; }
  html, body {
    width: 1200px;
    height: 1000px;
    overflow: hidden;
    background: var(--page);
  }
  .label {
    position: absolute;
    left: 110px;
    top: 190px;
    width: 980px;
    height: 620px;
    overflow: hidden;
    border-radius: 6px;
  }
  .label-art {
    position: absolute;
    inset: 0;
    background:
      linear-gradient(120deg,
        var(--sky) 0%,
        var(--royal) 18%,
        var(--green) 34%,
        var(--violet) 50%,
        var(--sky) 64%,
        var(--magenta) 80%,
        var(--orange) 100%);
  }
  .brand {
    position: absolute;
    left: 0;
    right: 0;
    top: 150px;
    text-align: center;
    color: var(--white);
    font-family: "Russo One", sans-serif;
    font-weight: 400;
    line-height: 1;
  }
  .brand-name {
    display: block;
    font-size: 168px;
    letter-spacing: 4px;
  }
  .brand-sub {
    display: block;
    margin-top: 10px;
    font-size: 62px;
    letter-spacing: 2px;
  }
  .product-type {
    position: absolute;
    left: 0;
    right: 0;
    top: 412px;
    text-align: center;
    font-family: "Russo One", sans-serif;
    font-size: 50px;
    line-height: 1;
    color: var(--white);
    -webkit-text-stroke: 2px var(--magenta);
    letter-spacing: 1px;
  }
  .info-band {
    position: absolute;
    left: 0;
    right: 0;
    bottom: 40px;
    height: 74px;
    background: var(--navy);
    display: flex;
    align-items: center;
    font-family: "Roboto Condensed", sans-serif;
    font-style: italic;
    font-weight: 800;
    color: var(--white);
  }
  .servings-count {
    height: 100%;
    width: 96px;
    background: var(--red);
    display: flex;
    align-items: center;
    justify-content: center;
    font-size: 48px;
    font-style: normal;
  }
  .servings-label {
    margin-left: 22px;
    font-size: 44px;
    letter-spacing: 1px;
  }
  .net-weight {
    margin-left: auto;
    margin-right: 30px;
    font-size: 26px;
  }
</style>
</head>
<body>
  <section class="label">
    <div class="label-art" role="img" aria-label="Colourful diagonal stripe pattern with paint splatters, circles and thin line shapes in blue, green, purple, pink and orange"></div>
    <h1 class="brand">
      <span class="brand-name">QUELVA</span>
      <span class="brand-sub">PERFORMANCE</span>
    </h1>
    <p class="product-type">[PRE-WORKOUT]</p>
    <div class="info-band">
      <span class="servings-count">30</span>
      <span class="servings-label">SERVINGS</span>
      <span class="net-weight">NET WT. 195g (6,87 oz.)</span>
    </div>
  </section>
</body>
</html>
```